Meridell Associates brouchure

I am attaching a sample of what I would like to be created in a vector format or format that I can send to a printer.

The Meridell Associates logo is the style I like.

Thanks, Gus

Industry/Entity Type

Printer

Font styles to use
Other font styles liked:
• please see attached

Requirements
Must have
• please create a format that I can provide to a printer for making a brochure
• UPDATE: please if possible, have the size be 10'' wide by 11'' tall
• with the brochure opening from top to bottom like a calendar
Nice to have
• I like where you are going with this, can you put an image on the top of the page and the text on the bottom of the page
• when you are holding the marketing piece, it should be 10'' wide by 5.5'' tall, after you open the cover page, then it becomes 10'' wide by 11'' tall
• the top page is an image and the lower page is the message..
• so when you view it you see a picture and then text
• the front cover should have the logo image -
• Meridell Associates
• the wording - cost effective resources for your practice
• cash back medical plans, 15% medical wellness discount
• on the inside pages 1-3 keep the tag line Meridell Associates / Practice Management
• the contact info on page 4
• the last page - Meridell Associates logo in the middle, then Practice Management on the bottom

```html
<!DOCTYPE html>
<html lang="en">
<head>
<meta charset="utf-8">
<title>Meridell Associates – Calendar Fold Brochure</title>
<link rel="stylesheet" href="https://fonts.googleapis.com/css2?family=Oswald:wght@400;500;600&family=PT+Sans+Narrow:wght@400;700&display=swap">
<style>
  :root {
    --blue: #1a8fe0;
    --blue-deep: #0f6fc4;
    --blue-light: #5db6f2;
    --sky: #cfe9fb;
    --grey-band: #8d8f92;
    --ink: #1d1d1f;
    --text-grey: #4a4a4a;
    --paper: #ffffff;
    --backdrop: #e4e4e8;
    --fold: #d3d6da;
  }
  * { box-sizing: border-box; margin: 0; padding: 0; }
  html, body { width: 1200px; height: 799px; overflow: hidden; }
  body { background: var(--backdrop); font-family: "PT Sans Narrow", "Arial Narrow", sans-serif; }

  /* 10in x 11in opened sheet, folding top to bottom */
  .sheet { position: absolute; left: 264px; top: 30px; width: 672px; height: 740px; display: flex; flex-direction: column; box-shadow: 0 6px 24px rgba(0,0,0,.18); }
  .panel { position: relative; width: 672px; height: 370px; background: var(--paper); overflow: hidden; }
  .panel + .panel { border-top: 1px solid var(--fold); }
  .panel svg.waves { position: absolute; left: 0; top: 0; width: 672px; height: 370px; }

  .brand-name { font-family: "Oswald", sans-serif; font-weight: 600; color: var(--blue); letter-spacing: .5px; }

  /* top page: cover image */
  .cover .brand-name { position: absolute; top: 12px; left: 0; width: 100%; text-align: center; font-size: 34px; line-height: 1.2; }
  .ribbon { position: absolute; left: 136px; top: 66px; width: 400px; height: 32px; background: var(--blue); color: #fff; font-family: "Oswald", sans-serif; font-size: 17px; font-weight: 500; display: flex; align-items: center; justify-content: center; transform: rotate(-3deg); box-shadow: 0 2px 4px rgba(0,0,0,.25); z-index: 2; }
  .photo { position: absolute; left: 0; top: 112px; width: 672px; height: 180px; background: linear-gradient(120deg, #f2f4f6 0%, #d9dee3 30%, #6b5a52 50%, #e8ecef 72%, #c9d0d6 100%); }
  .badge { position: absolute; left: 34px; top: 196px; width: 146px; height: 146px; border-radius: 50%; background: var(--blue); border: 5px solid #fff; color: #fff; font-family: "Oswald", sans-serif; text-align: center; display: flex; flex-direction: column; justify-content: center; line-height: 1; box-shadow: 0 2px 6px rgba(0,0,0,.2); }
  .badge .pct { font-size: 42px; font-weight: 600; }
  .badge .txt { font-size: 17px; font-weight: 500; line-height: 1.05; }
  .offer { position: absolute; right: 44px; top: 262px; color: #fff; font-family: "Oswald", sans-serif; font-size: 28px; font-weight: 500; line-height: 1.1; text-align: center; }
  .web { position: absolute; left: 300px; bottom: 8px; color: #fff; font-family: "Oswald", sans-serif; font-size: 15px; font-weight: 600; letter-spacing: 1px; }

  /* bottom page: message */
  .message .brand-row { position: absolute; top: 16px; left: 0; width: 100%; display: flex; align-items: center; justify-content: center; gap: 14px; }
  .message .brand-row .rule { width: 70px; height: 3px; background: var(--ink); }
  .message .brand-name { font-size: 26px; line-height: 1.2; }
  .intro-box { position: absolute; left: 40px; top: 78px; width: 300px; height: 108px; border: 2px solid var(--blue); border-radius: 4px; }
  .intro-box p { position: absolute; top: -9px; left: 12px; right: 12px; background: var(--paper); font-style: italic; font-size: 13px; color: var(--ink); text-align: center; line-height: 1.2; padding: 0 6px; }
  .benefits { position: absolute; top: 40px; left: 0; width: 100%; display: flex; justify-content: space-around; }
  .benefit { text-align: center; font-family: "Oswald", sans-serif; font-size: 11px; font-weight: 500; color: var(--ink); }
  .benefit .dot { width: 30px; height: 30px; border-radius: 50%; background: var(--blue); margin: 0 auto 6px; display: flex; align-items: center; justify-content: center; }
  .grey-band { position: absolute; left: 370px; top: 96px; width: 262px; height: 72px; background: var(--grey-band); color: #fff; font-style: italic; font-size: 13px; line-height: 1.25; padding: 10px 14px; text-align: center; }
  .contact-title { position: absolute; left: 70px; top: 226px; font-family: "Oswald", sans-serif; font-weight: 600; font-size: 18px; color: var(--blue); }
  .contact-divider { position: absolute; left: 206px; top: 214px; width: 1px; height: 60px; background: #999; }
  .contact-list { position: absolute; left: 220px; top: 214px; list-style: none; font-size: 11px; color: var(--text-grey); }
  .contact-list li { display: flex; align-items: center; gap: 6px; height: 20px; }
  .call-now { position: absolute; left: 40px; bottom: 22px; color: #fff; font-family: "Oswald", sans-serif; display: flex; align-items: baseline; gap: 10px; }
  .call-now .label { font-size: 14px; font-weight: 500; }
  .call-now .phone { font-size: 30px; font-weight: 600; }
</style>
</head>
<body>
<main class="sheet">

  <section class="panel cover">
    <h1 class="brand-name">Meridell Associates</h1>
    <div class="ribbon">Cost Effective Resources For Your Practice</div>
    <div class="photo" role="img" aria-label="Photo of two smiling businesswomen working together at a desk with a laptop"></div>

    <svg class="waves" viewBox="0 0 672 370" aria-hidden="true">
      <path d="M0 262 C200 238 420 286 672 236 L672 370 L0 370 Z" fill="var(--sky)"/>
      <path d="M0 274 C200 250 420 298 672 250 L672 370 L0 370 Z" fill="var(--blue-light)"/>
      <path d="M0 286 C210 262 420 310 672 264 L672 370 L0 370 Z" fill="var(--blue)"/>
      <path d="M0 338 C220 326 440 350 672 332" fill="none" stroke="#fff" stroke-width="1.5" opacity=".7"/>
      <path d="M0 346 C220 334 440 360 672 342 L672 370 L0 370 Z" fill="var(--blue-deep)" opacity=".35"/>
    </svg>

    <div class="badge">
      <span class="pct">15%</span>
      <span class="txt">WELLNESS<br>MEDICAL<br>DISCOUNT</span>
    </div>
    <p class="offer">CASH BACK<br>MEDICAL PLANS</p>
    <p class="web">www.meridellassoc.com</p>
  </section>

  <section class="panel message">
    <svg class="waves" viewBox="0 0 672 370" aria-hidden="true">
      <path d="M0 200 C180 176 400 222 672 186 L672 370 L0 370 Z" fill="var(--sky)"/>
      <path d="M0 208 C190 184 400 232 672 196 L672 370 L0 370 Z" fill="var(--blue-light)"/>
      <path d="M0 214 C190 190 400 238 672 202 L672 370 L0 370 Z" fill="var(--paper)"/>
      <path d="M0 288 C200 270 420 306 672 280 L672 370 L0 370 Z" fill="var(--blue-light)"/>
      <path d="M0 298 C200 278 420 318 672 290 L672 370 L0 370 Z" fill="var(--blue)"/>
      <path d="M0 336 C220 324 440 348 672 330 L672 370 L0 370 Z" fill="var(--blue-deep)" opacity=".35"/>
    </svg>

    <div class="brand-row">
      <span class="rule"></span>
      <span class="brand-name">Meridell Associates</span>
      <span class="rule"></span>
    </div>

    <div class="intro-box">
      <p>Meridell Associates Practice Management is a relationship that gives your practice</p>
      <div class="benefits">
        <div class="benefit">
          <div class="dot"><svg width="16" height="16" viewBox="0 0 18 18"><circle cx="9" cy="9" r="7" fill="none" stroke="#fff" stroke-width="2"/><path d="M9 4v5h4" fill="none" stroke="#fff" stroke-width="2"/></svg></div>TIME</div>
        <div class="benefit">
          <div class="dot"><svg width="16" height="16" viewBox="0 0 18 18"><text x="9" y="14" text-anchor="middle" fill="#fff" font-size="15" font-family="Oswald, sans-serif">$</text></svg></div>COST</div>
        <div class="benefit">
          <div class="dot"><svg width="16" height="16" viewBox="0 0 18 18"><path d="M9 1l2.4 5 5.4.6-4 3.7 1.1 5.4L9 13l-4.9 2.7 1.1-5.4-4-3.7 5.4-.6z" fill="#fff"/></svg></div>REWARDS</div>
      </div>
    </div>

    <div class="grey-band">Proven guidance in group benefits, payroll, human resources, workers compensation, 401(k) and more</div>

    <h2 class="contact-title">CONTACT US</h2>
    <span class="contact-divider"></span>
    <ul class="contact-list">
      <li><svg width="9" height="11" viewBox="0 0 9 11"><path d="M4.5 0a4 4 0 0 1 4 4c0 3-4 7-4 7s-4-4-4-7a4 4 0 0 1 4-4z" fill="var(--blue)"/></svg>PO Box 4410 Lakeview FL 32801</li>
      <li><svg width="9" height="11" viewBox="0 0 9 11"><rect x="1" y="0" width="7" height="11" rx="1.5" fill="var(--blue)"/></svg>866.555.0187</li>
      <li><svg width="10" height="8" viewBox="0 0 10 8"><rect width="10" height="8" fill="var(--blue)"/><path d="M0 0l5 4 5-4" fill="none" stroke="#fff"/></svg>info@meridell.com</li>
    </ul>

    <p class="call-now"><span class="label">CALL NOW TO FIND OUT HOW:</span><span class="phone">407.555.0142</span></p>
  </section>

</main>
</body>
</html>
```